Create a Graphic About YOURSELF and PixelHarbor

PixelHarbor would like you (designers) to create an awesome graphic to promote YOURSELF and your profile on PixelHarbor!

Your graphic should communicate your name, your services and should mention PixelHarbor.

The design should be perfect for sharing on Chatterly. Here's an example of what we'd like http://blog.pixelharbor-example.ca/article/333/pixelharbor-launches-3000-hire-me-social-design-contest

Once you submitted your design, we'd love you to share the design ('advertisement') and promote yourself and PixelHarbor to your friends and potential customers. So make your submissions great and get your friends to vote for your design by 'Liking' it on Chatterly!

Prizes:
$1500 - "PixelHarbor Community" prize awarded to the designer with the most Chatterly 'Likes'
5 x $50 for the next 5 'most liked' designs on Chatterly

$1000 - "Hire Me" prize awarded to the designer who receives the most client invites
5 x $50 for the next 5 'most invited' designers

In summary, this is a great opportunity for you to increase your exposure to PixelHarbor customers and win cash prizes. Show off your design skills and get hired by PixelHarbor customers from around the world!

Target Market(s)

Fans, friends and customers of YOU

Industry/Entity Type

Cash

Requirements
Must have
• 1) Include your PixelHarbor user name on the graphic so customers can find you in the PixelHarbor Designer Directory
2) Include the tagline "Hire Me on PixelHarbor.com!" in your graphic design.
3) Share your design's URL on our Chatterly wall at http://chatterly-example.com/pixelharbor and get your friends to 'like' your design.
Nice to have
• 1) Include a tagline that expresses your design approach/philosophy
2) Artwork dimensions: 403 x 403 px
3) You can submit more than 1 design!
Should not have
• You must own the copyright of any images you use including stock imagery.

```html
<!DOCTYPE html>
<html lang="en">
<head>
<meta charset="utf-8">
<title>Hire Me — Epiphany Studio</title>
<link rel="stylesheet" href="https://fonts.googleapis.com/css2?family=Caladea&display=swap">
<style>
  :root {
    --burst-red: #d92b28;
    --burst-orange: #f07a2e;
    --burst-edge: #ffe414;
    --ink: #1c1410;
    --headline: #fff6cc;
    --cat-dark: #1d3a3a;
    --cat-teal: #3f7d74;
    --cat-gold: #9c8640;
    --page: #ffffff;
  }
  html, body {
    margin: 0;
    padding: 0;
    width: 1200px;
    height: 900px;
    overflow: hidden;
    background: var(--page);
  }
  .canvas {
    display: block;
    width: 1200px;
    height: 900px;
  }
  .burst {
    fill: url(#burstFill);
    stroke: var(--burst-edge);
    stroke-width: 9;
    stroke-linejoin: miter;
  }
  .service {
    font-family: "Caladea", serif;
    font-size: 21px;
    fill: var(--ink);
  }
  .service--small { font-size: 17px; }
  .service--tall { font-size: 23px; }
  .studio-name {
    font-family: "Caladea", serif;
    font-size: 28px;
    fill: var(--ink);
  }
  .headline {
    font-family: "Caladea", serif;
    font-size: 76px;
    letter-spacing: -1px;
    fill: var(--headline);
  }
  .artwork-shadow { fill: rgba(0, 0, 0, 0.3); filter: url(#softShadow); }
  .artwork { fill: url(#artworkFill); }
</style>
</head>
<body>
<svg class="canvas" viewBox="0 0 1200 900" xmlns="http://www.w3.org/2000/svg">
  <defs>
    <linearGradient id="burstFill" x1="0" y1="0" x2="1" y2="0">
      <stop offset="0" stop-color="var(--burst-red)"/>
      <stop offset="1" stop-color="var(--burst-orange)"/>
    </linearGradient>
    <linearGradient id="artworkFill" x1="0" y1="0" x2="1" y2="0">
      <stop offset="0" stop-color="var(--cat-teal)"/>
      <stop offset="0.55" stop-color="var(--cat-dark)"/>
      <stop offset="1" stop-color="var(--cat-gold)"/>
    </linearGradient>
    <filter id="softShadow" x="-10%" y="-40%" width="120%" height="180%">
      <feGaussianBlur stdDeviation="8"/>
    </filter>
    <path id="headlineArc" d="M 485 355 Q 650 300 815 385"/>
  </defs>

  <polygon class="burst" points="
    140,100 440,260 492,100 595,225 752,12 750,215 922,188 855,300
    1050,330 935,445 1075,550 870,560 915,740 760,600 700,760 590,700
    490,880 455,620 350,700 340,560 130,595 265,480 118,355 345,325"/>

  <g role="img" aria-label="Illustration of a cheetah sprinting to the right, its spotted coat rendered in glowing teal and gold">
    <rect class="artwork-shadow" x="160" y="412" width="850" height="80" rx="40"/>
    <rect class="artwork" x="150" y="400" width="850" height="78" rx="39"/>
  </g>

  <g class="services">
    <text class="service" transform="translate(298 222) rotate(40)" text-anchor="middle">Packaging &amp; Labels</text>
    <text class="service" transform="translate(515 190)" text-anchor="middle">Ads</text>
    <text class="service" transform="translate(700 160) rotate(-62)" text-anchor="middle">Graphic Design</text>
    <text class="service" transform="translate(852 236) rotate(30)" text-anchor="middle">Menus</text>
    <text class="service service--small" transform="translate(984 346) rotate(15)" text-anchor="middle">Signs</text>
    <text class="service" transform="translate(215 386) rotate(22)" text-anchor="middle">Flyers</text>
    <text class="service service--small" transform="translate(965 508) rotate(15)" text-anchor="middle">Stationary</text>
    <text class="service service--small" transform="translate(260 558) rotate(-12)" text-anchor="middle">PixelHarbor.com</text>
    <text class="service" transform="translate(388 646) rotate(-62)" text-anchor="middle">Logos</text>
    <text class="service service--tall" transform="translate(518 740) rotate(-90)" text-anchor="middle">Illustrations</text>
    <text class="service" x="668" y="660" text-anchor="middle">And</text>
    <text class="service" x="672" y="696" text-anchor="middle">More</text>
    <text class="service" transform="translate(840 630) rotate(55)" text-anchor="middle">Business Cards</text>
  </g>

  <text class="headline" text-anchor="middle">
    <textPath href="#headlineArc" startOffset="50%">Hire Me!!!</textPath>
  </text>

  <text class="studio-name" transform="translate(582 562) rotate(18)" text-anchor="middle">Epiphany Studio</text>
</svg>
</body>
</html>
```